Pemberton Dialworks Business Card Design

Double Sided Business Card Design for a Locksmith company specializing in Safecracking, safe & vault service.

```html
<!DOCTYPE html>
<html lang="en">
<head>
<meta charset="utf-8">
<title>Pemberton Dialworks Business Card</title>
<link rel="stylesheet" href="https://fonts.googleapis.com/css2?family=Montserrat:wght@400;600;800&display=swap">
<style>
  :root {
    --backdrop: #9a9a9a;
    --ink: #050505;
    --paper: #ffffff;
    --brand-green: #237a3b;
    --text-light: #f2f2f2;
    --text-dark: #1a1a1a;
  }
  html, body {
    margin: 0;
    padding: 0;
    width: 1200px;
    height: 900px;
    overflow: hidden;
    background: var(--backdrop);
    font-family: "Montserrat", Arial, sans-serif;
  }
  .canvas {
    position: relative;
    width: 1200px;
    height: 900px;
  }
  .card {
    position: absolute;
    width: 520px;
    height: 300px;
    border-radius: 26px;
    overflow: hidden;
    box-shadow: 0 10px 24px rgba(0,0,0,0.25);
  }

  /* Back side */
  .card--back {
    left: 90px;
    top: 110px;
    background: var(--ink);
    display: flex;
    align-items: center;
    justify-content: center;
    gap: 18px;
  }
  .brand-dot {
    width: 64px;
    height: 64px;
    border-radius: 50%;
    background: var(--brand-green);
    flex: none;
  }
  .brand-name {
    margin: 0;
    color: var(--brand-green);
    font-weight: 800;
    font-size: 30px;
    line-height: 1.02;
    letter-spacing: 1px;
    text-transform: uppercase;
  }

  /* Front side */
  .card--front {
    left: 590px;
    top: 480px;
    background: var(--paper);
  }
  .card__shapes {
    position: absolute;
    inset: 0;
  }
  .front-brand {
    position: absolute;
    right: 28px;
    top: 28px;
    display: flex;
    align-items: center;
    gap: 14px;
  }
  .front-brand .brand-name {
    font-size: 17px;
    text-align: right;
  }
  .front-brand .brand-dot {
    width: 96px;
    height: 96px;
  }
  .person {
    position: absolute;
    left: 32px;
    top: 140px;
  }
  .person__name {
    margin: 0;
    color: var(--brand-green);
    font-weight: 800;
    font-size: 24px;
    letter-spacing: 0.5px;
    text-transform: uppercase;
  }
  .person__role {
    margin: 2px 0 0;
    color: var(--text-dark);
    font-size: 13px;
  }
  .contact {
    position: absolute;
    left: 232px;
    top: 196px;
    color: var(--text-light);
    font-size: 11.5px;
    line-height: 1.35;
  }
  .contact p { margin: 0; }
  .contact ul {
    list-style: none;
    margin: 6px 0 0;
    padding: 0;
  }
  .contact li {
    display: flex;
    align-items: center;
    gap: 7px;
    margin-bottom: 2px;
  }
  .contact svg { width: 12px; height: 12px; flex: none; }
</style>
</head>
<body>
<main class="canvas">

  <section class="card card--back" aria-label="Card back">
    <span class="brand-dot"></span>
    <h1 class="brand-name">Pemberton<br>Dialworks</h1>
  </section>

  <section class="card card--front" aria-label="Card front">
    <svg class="card__shapes" viewBox="0 0 520 300" width="520" height="300">
      <path d="M120 300 C150 210 260 150 400 140 C470 135 520 110 520 60 L520 300 Z" fill="var(--ink)"/>
      <path d="M98 300 C132 206 245 143 390 132" fill="none" stroke="var(--brand-green)" stroke-width="6"/>
    </svg>

    <div class="front-brand">
      <h2 class="brand-name">Pemberton<br>Dialworks</h2>
      <span class="brand-dot"></span>
    </div>

    <div class="person">
      <h2 class="person__name">Owen Hartley</h2>
      <p class="person__role">Founder &amp; CEO</p>
    </div>

    <address class="contact" style="font-style:normal">
      <p>1234 First Line Address</p>
      <p>5678 Second Line Address</p>
      <ul>
        <li>
          <svg viewBox="0 0 12 12"><path d="M2 1 L4.5 1 L5.5 3.5 L4 4.5 C4.7 6 6 7.3 7.5 8 L8.5 6.5 L11 7.5 L11 10 C6 10.5 1.5 6 2 1 Z" fill="var(--brand-green)"/></svg>
          1234567890
        </li>
        <li>
          <svg viewBox="0 0 12 12"><rect x="1" y="2.5" width="10" height="7" fill="var(--brand-green)"/><path d="M1 2.5 L6 6.5 L11 2.5" fill="none" stroke="var(--ink)" stroke-width="1"/></svg>
          info@yourmail.com
        </li>
        <li>
          <svg viewBox="0 0 12 12"><circle cx="6" cy="6" r="5" fill="none" stroke="var(--brand-green)" stroke-width="1.4"/><path d="M1 6 H11 M6 1 V11" stroke="var(--brand-green)" stroke-width="1"/></svg>
          www.yourwebsite.com
        </li>
      </ul>
    </address>
  </section>

</main>
</body>
</html>
```